Industrial Inspection & Testing Company Needs Brochure

We need a brochure design for a company based in Western Pennsylvania, USA. Our company performs services mainly in industrial sites. These can include manufacturing, health & medical, power generation, and more. We use infrared thermography, vibration analysis, ultrasonic thickness testing, dynamic balancing and other practices to provide predictive maintenance to our customers. Please see our website for a more thorough explanation of our services. www.kortalinspect.com

Complete list of services:

Infrared Thermal Imaging
Vibration Analysis
High Temperature Video & Photography
High Speed Video
Laser Alignment
Dynamic Balancing
Motor Meggering
Leak Detection
Ultrasonic Thickness Testing
Oil Analysis

KRT, LLC - P.O. Box 4738 - Maple Hollow, PA 15842
Phone: 555-318-4471 / Fax: 555-318-4479

MISSION

KRT, LLC will provide the highest quality, cost effective, world class PdM services in the industry. Our commitment to continuing education and growth will afford our engineers the tools needed to stay on the cutting edge of technology. We believe in the implementation of Predictive Maintenance services to increase overall equipment reliability, reduce costs and improve profitability. Our goal is to provide continuous improvements to these processes. The company will network with various industry professionals to offer the widest range of equipment, training and reliability services available. Meeting these goals will ensure the company’s longevity and allow our valued customers to achieve the cost reduction goals that are needed in today’s competitive marketplace.
HISTORY
KRT, LLC was founded in March 1984, which emerged from the Granite Forge Industries’ Laboratory Campus, Monroeville, Pennsylvania. Its founders headed the Thermography and Photoinstrumentation Department of that facility.
While at the G. F. Industries Laboratory Campus, they established the utilization of thermography as a valuable tool for evaluating equipment and facilities in the steel industry. Their work set the standards for the use of thermography in the steel industry that continues today with KRT. Although the original thermographic equipment was crude, bulky and slow, KRT has maintained its position as an industry leader. Today KRT uses the most technologically advanced infrared systems available for on-site nondestructive industrial inspections.
In addition, while at G. F. Industries Laboratory, the founders of KRT pioneered the use of photographic cameras and high-speed motion pictures as another form of a predictive and preventative maintenance tool. Specially constructed camera systems with thermal protective housings were developed for inspecting blast furnace interior stockline armor areas, stove domes, and other high-temperature areas.
Today KRT remains on the cutting-edge in providing a wide range of nondestructive inspection services to industry.

***All of the photos and documents attached were either shot by us or purchased stock photos***

I realize that only a few images might be used, I just wanted to upload many to give designers a broad range to choose from.

Target Market(s)

Large industrial customers who use large amounts of electricity, heavy duty machinery, or both.

Industry/Entity Type

Industrial

Requirements
Must have
• Need a 3 full page tri-fold design (not skinny column tri-fold)

Contact information for our company, list of our services, our logo (possible redesign of logo), photos from our inspections that will be attached.
Nice to have
• List of services, breif explanation of each with graphical representation, contact information

```html
<!DOCTYPE html>
<html lang="en">
<head>
<meta charset="utf-8">
<title>KRT, LLC — Inside Spread</title>
<link href="https://fonts.googleapis.com/css2?family=Questrial&display=swap" rel="stylesheet">
<style>
  :root{
    --green:#4d9b37;
    --green-dark:#3d8a2c;
    --purple:#55369a;
    --orange:#e8561d;
    --blue:#3b4ea3;
    --yellow:#f3e11b;
    --cream:#f6f3e4;
    --cream-warm:#fbf7d2;
    --ink:#2b2b2b;
    --stage:#e9e9ec;
  }
  *{box-sizing:border-box;margin:0;padding:0}
  html,body{width:1200px;height:769px;overflow:hidden;background:var(--stage)}
  body{font-family:"Questrial",sans-serif;color:var(--ink);position:relative}
  .spread{position:absolute;left:45px;top:95px;width:1110px;height:580px;display:flex;box-shadow:0 8px 28px rgba(0,0,0,.18)}
  .panel{position:relative;width:370px;height:100%;overflow:hidden}
  .trim-bottom{position:absolute;left:0;right:0;bottom:0;height:22px;background:var(--green)}
  .trim-top{position:absolute;left:0;right:0;top:0;height:16px;background:var(--green)}
  .photo{position:absolute}
  .frame-purple{border:5px solid var(--purple)}
  .frame-green{border:5px solid var(--green)}

  /* Panel 1 */
  .panel--mission{background:var(--green)}
  .mission{position:absolute;left:20px;top:22px;right:16px;color:#fff}
  .mission__title{font-size:24px;font-weight:400;margin-bottom:6px}
  .mission__title span{color:var(--yellow)}
  .mission__body{columns:2;column-gap:14px;font-size:7.6px;line-height:1.45;text-align:justify}
  .thermal-field{left:0;top:190px;width:370px;height:368px;background:radial-gradient(ellipse at 30% 40%,#e6f23a 0%,#8fd63a 30%,#2fa65a 55%,#1f6f7a 72%,#6b2a9e 100%)}
  .thermo-band{position:absolute;left:0;top:340px;width:370px;height:190px;background:rgba(255,255,255,.62)}
  .thermo-inset{left:190px;top:265px;width:150px;height:115px;border:5px solid var(--yellow);background:linear-gradient(135deg,#3a1f7a 0%,#d8402b 45%,#f6a22a 70%,#f7e06a 100%)}
  .thermo{position:absolute;left:20px;top:392px;width:320px}
  .thermo__title{font-size:20px;color:var(--orange);font-weight:400;margin-bottom:6px}
  .thermo p{font-size:8.5px;line-height:1.4}
  .list{list-style:none;font-size:8.5px;line-height:1.45;margin:2px 0 4px}
  .list li::before{content:"";display:inline-block;width:4px;height:4px;border-radius:50%;background:var(--orange);margin:0 6px 1px 2px}
  .thermo .web{font-weight:700}

  /* Panel 2 */
  .panel--condition{background:var(--cream)}
  .condition{position:absolute;left:22px;top:32px;right:20px}
  .section-title{font-size:19px;line-height:1.05;color:var(--orange);font-weight:400;margin-bottom:8px}
  .intro{font-size:8.5px;line-height:1.4}
  .hero-plant{left:20px;top:150px;width:330px;height:250px;background:linear-gradient(160deg,#8cc3e6 0%,#4aa0d8 35%,#e0b84a 60%,#9aa3ab 100%)}
  .thumb{top:412px;width:104px;height:100px}
  .thumb--a{left:20px;background:linear-gradient(180deg,#8fb8d8,#7a6a55)}
  .thumb--b{left:133px;background:linear-gradient(180deg,#5d8fc4,#3f4b58)}
  .thumb--c{left:246px;background:linear-gradient(180deg,#3f7fc8,#6c7f92)}

  /* Panel 3 */
  .panel--precision{background:linear-gradient(90deg,var(--cream),var(--cream-warm))}
  .precision{position:absolute;left:20px;top:30px;width:175px}
  .precision .section-title{color:var(--blue)}
  .gear-a{left:210px;top:22px;width:150px;height:92px;background:linear-gradient(135deg,#c9c2b5,#6f6a62)}
  .gear-b{left:200px;top:122px;width:160px;height:100px;background:linear-gradient(135deg,#8a8a86,#3a3936)}
  .tank{left:14px;top:160px;width:180px;height:115px;background:linear-gradient(180deg,#b7c6d6,#7f8a92)}
  .video{position:absolute;left:205px;top:236px;width:155px}
  .video .section-title{margin-bottom:5px}
  .video p{font-size:8px;line-height:1.4}
  .video .list{font-size:8px}
  .furnace{left:14px;top:290px;width:180px;height:245px;background:linear-gradient(180deg,#5aa5d8 0%,#9ec7e4 40%,#8a5a3a 75%,#5b4030 100%)}
</style>
</head>
<body>
<main class="spread">

  <section class="panel panel--mission">
    <div class="mission">
      <h2 class="mission__title">Our <span>MISSION</span></h2>
      <p class="mission__body">KRT, LLC will provide the highest quality, cost effective, world class PdM services in the industry. Our commitment to continuing education and growth will afford our engineers the tools needed to stay on the cutting edge of technology. We believe in the implementation of Predictive Maintenance services to increase overall equipment reliability, reduce costs and improve profitability. Our goal is to provide continuous improvements to these processes. The company will network with various industry professionals to offer the widest range of equipment, training and reliability services available. Meeting these goals will ensure the company’s longevity and allow our valued customers to achieve the cost reduction goals that are needed in today’s competitive marketplace.</p>
    </div>
    <div class="photo thermal-field" role="img" aria-label="Infrared thermal image of industrial equipment in green, yellow and purple tones"></div>
    <div class="thermo-band"></div>
    <div class="photo thermo-inset" role="img" aria-label="Thermal image of an electrical panel"></div>
    <div class="thermo">
      <h3 class="thermo__title">Thermography Services</h3>
      <p>KRT offers a wide range of Infrared Thermography Services, which includes:</p>
      <ul class="list">
        <li>Building Inspections</li>
        <li>Electrical Inspections</li>
        <li>Roof Inspections</li>
        <li>Infrared Thermal Imaging</li>
      </ul>
      <p>For more details visit <span class="web">www.kortalinspect.com</span>.</p>
    </div>
    <div class="trim-bottom"></div>
  </section>

  <section class="panel panel--condition">
    <div class="trim-top"></div>
    <div class="condition">
      <h3 class="section-title">Condition Monitoring &amp; Predictive Maintenance Services</h3>
      <p class="intro">We provide the following Condition Monitoring &amp; Predictive Maintenance Services:</p>
      <ul class="list">
        <li>Vibration Analysis</li>
        <li>Oil Analysis</li>
        <li>Ultrasonic Leak Detection</li>
        <li>Ultrasonic Thickness Testing</li>
      </ul>
    </div>
    <div class="photo hero-plant frame-purple" role="img" aria-label="Pump station with blue piping and yellow walkways"></div>
    <div class="photo thumb thumb--a frame-purple" role="img" aria-label="Industrial plant exterior"></div>
    <div class="photo thumb thumb--b frame-purple" role="img" aria-label="Refinery towers"></div>
    <div class="photo thumb thumb--c frame-purple" role="img" aria-label="Power plant against blue sky"></div>
    <div class="trim-bottom"></div>
  </section>

  <section class="panel panel--precision">
    <div class="trim-top"></div>
    <div class="precision">
      <h3 class="section-title">Precision Maintenance Services</h3>
      <ul class="list">
        <li>Precision Laser Alignment</li>
        <li>Balancing</li>
      </ul>
      <p class="intro">We provide precision maintenance services, including Precision Laser Alignment and Balancing.</p>
    </div>
    <div class="photo gear-a frame-green" role="img" aria-label="Bearing and shaft assembly"></div>
    <div class="photo gear-b frame-green" role="img" aria-label="Gear inside a housing"></div>
    <div class="photo tank frame-green" role="img" aria-label="Industrial storage tanks"></div>
    <div class="video">
      <h3 class="section-title">Video Inspection Services</h3>
      <p>KRT offers a wide range of Video and Photographic Inspections including:</p>
      <ul class="list">
        <li>High Temperature</li>
        <li>High Speed</li>
        <li>Slow Motion</li>
        <li>Gearing</li>
        <li>Piping</li>
        <li>Duct Work</li>
        <li>and much more</li>
      </ul>
      <p>Call 555-318-4471 today for your <strong>video inspection</strong> needs. We custom build delivery devices for the most challenging of applications.</p>
    </div>
    <div class="photo furnace frame-green" role="img" aria-label="Blast furnace structure under blue sky"></div>
    <div class="trim-bottom"></div>
  </section>

</main>
</body>
</html>
```